Delivery Docket urgent plus require many other designs for more stationary after this.

We need a new delivery docket design urgently as the one we have needs updating and we have changed our company name. Please do not copy the one I have uploaded as we do not feel this looks professional enough. I uploaded it as a few designers requested to see what we are currently using thank you.
It is quite complex in that we need a range of information to be on the one docket.
We are a Transport Company based in Australia that has a wide variety of items that we deliver such as water, sand and gravels and heavy equipment transport.
We would prefer to keep this design to A5 size as we will get them made into books. We are looking for a modern professional look. Although it is only a delivery docket this is given to all our customers so needs to look impressive.

We need our new logo on the docket (PRW). There will also need to be areas for our address and contact numbers, email etc these will be supplied to the winning designer to make the final adjustments so for now just put something generic in these spaces.
Needs to have an area for customer details, purchase order number, date and docket number (docket number to be in red)
Needs a section where we can list the type of product / and or service that has been provided and the amount / qty usually 3 lines will be enough for this. Need area under this where the customer can sign name and print name to say that the goods / and or services have been received.

Also required somewhere on the docket are the words, Tax Invoice will be issued based on the information provided on this docket. Conditions on back of page

We then need a separate section on the same page which we will use internally that the staff member can tear off and hand into the office. On this section it needs to have area where the driver can list km at start of job and at end with space to calculate km travelled, details of fuel purchased eg amount and litres, vehicle that is being used. also need to log down wheel bearing temps.
prime mover needs spaces as follows
Steer axel FL____________ Steer axel FR _________ 1st drive axel L_______
1st drive axel R_________ 2nd drive axel L_______ 2nd drive axel R________

For the trailers need something similar x 2 as have 2 trailers
1st axel DS_________ 1st axel PS_________ 2nd axel DS__________
2nd axel PS_________ 3rd axel DS_________ 3rd axel PS__________

I have included a few examples of designs we have used in past and ones that we like so you can get an idea of the colours we prefer, I have included some of the designs we are currently receiving for our logo that I like so you can get idea again of colours we prefer. There is much more we need designed also such as time sheets, more delivery dockets and letter heads so there is a lot of more work available to the winning designer.

Thank you

Target Market(s)

Customers

Font styles to use
Serif
Sans Serif

Colors

Designer to choose colors to be used in the design.

Requirements
Should not have
• Please don't copy old docket as we do not like it and nned new info on new design thank you

```html
<!DOCTYPE html>
<html lang="en">
<head>
<meta charset="utf-8">
<title>PRW Delivery Docket</title>
<link rel="stylesheet" href="https://fonts.googleapis.com/css2?family=Arimo:ital,wght@0,400;0,700;1,700&family=Roboto+Condensed:ital,wght@1,700&display=swap">
<style>
  :root {
    --paper: #f2efda;
    --blue: #5585c1;
    --blue-soft: rgba(85, 133, 193, 0.88);
    --ink: #161616;
    --white: #ffffff;
    --cream: #f3efd3;
    --red: #d8201e;
    --photo-light: #d9d8cb;
    --photo-dark: #8f8f86;
  }
  * { box-sizing: border-box; margin: 0; padding: 0; }
  html, body { width: 852px; height: 1200px; overflow: hidden; }
  body {
    position: relative;
    background: var(--paper);
    font-family: "Arimo", Arial, sans-serif;
    color: var(--ink);
  }
  .abs { position: absolute; }

  .header {
    left: 14px; top: 0; width: 829px; height: 172px;
    background: var(--blue);
    border-radius: 0 0 12px 12px;
  }
  .brand {
    left: 42px; top: 45px; width: 160px; height: 101px;
    background: var(--white); border-radius: 14px;
    display: flex; align-items: center; justify-content: center;
    font-weight: 700; font-size: 52px; color: #000;
  }
  .contact {
    right: 29px; top: 36px; text-align: right;
    font-size: 16px; line-height: 20px; color: #111;
  }

  .truck-photo {
    left: 31px; top: 275px; width: 789px; height: 587px;
    background: linear-gradient(180deg, var(--photo-light) 0%, #b8b7aa 45%, var(--photo-dark) 70%, #c9c8bb 100%);
  }

  .panel { background: var(--blue); border-radius: 18px; }
  .panel-title { font-weight: 700; font-size: 16px; }
  .field {
    position: absolute; display: flex; align-items: flex-end;
    font-size: 15px; white-space: nowrap;
  }
  .field .line { flex: 1; border-bottom: 1.4px solid #1d2a3a; margin-left: 3px; height: 14px; }

  .customer { left: 42px; top: 227px; width: 489px; height: 119px; }
  .order { left: 560px; top: 227px; width: 250px; height: 119px; }
  .docket-no {
    left: 98px; top: 81px; width: 129px; height: 33px;
    background: var(--cream); border-radius: 3px;
    color: var(--red); font-weight: 700; font-size: 21px;
    display: flex; align-items: center; justify-content: center;
  }

  .services {
    left: 47px; top: 393px; width: 763px; height: 172px;
    background: var(--blue-soft); border-radius: 34px;
  }
  .services .divider { left: 470px; top: 25px; width: 1.6px; height: 135px; background: #1d2a3a; }
  .services .rule { height: 1.4px; background: #1d2a3a; }
  .col-head { font-weight: 700; font-size: 17px; top: 4px; }

  .tax-note {
    left: 0; width: 852px; top: 590px; text-align: center;
    font-family: "Roboto Condensed", "Arial Narrow", sans-serif;
    font-style: italic; font-weight: 700; font-size: 19px; line-height: 26px;
  }

  .print-name {
    left: 95px; top: 685px; width: 268px; height: 48px;
    background: var(--cream); border-radius: 10px 0 0 10px;
    font-size: 14px; padding: 5px 0 0 20px;
  }
  .signed {
    left: 357px; top: 685px; width: 402px; height: 48px;
    background: var(--blue); border-radius: 6px;
    font-weight: 700; font-size: 17px; padding: 5px 0 0 47px;
  }

  .tear-line { left: 14px; top: 777px; width: 824px; border-top: 2px dashed #111; }

  .company-bar {
    left: 61px; top: 817px; width: 728px; height: 35px;
    background: var(--blue); border-radius: 18px;
    text-align: center; font-weight: 700; font-size: 27px; line-height: 35px;
  }

  .vehicle { left: 68px; top: 887px; width: 722px; height: 85px; border-radius: 22px; }
  .vehicle .field { font-size: 14.5px; }

  .axles { top: 998px; width: 352px; height: 154px; border-radius: 60px; }
  .axles.prime { left: 65px; }
  .axles.trailer { left: 441px; }
  .axle-label { width: 100%; text-align: center; font-size: 12px; }
  .axles .field { font-size: 12px; }
  .axles .field .line { height: 10px; }
</style>
</head>
<body>

<header class="abs header"></header>
<div class="abs brand">PRW</div>
<address class="abs contact" style="font-style:normal">
  Depot 4, 27<br>Ironbark Road<br>Contac Numbers: 5550148, 5550162<br>office@prwhaul.au<br>www.prwhaul.au
</address>

<div class="abs truck-photo" role="img" aria-label="Sketch-style photo of a road train truck on a dusty road"></div>

<section class="abs panel customer">
  <div class="abs panel-title" style="left:14px;top:8px">COSTUMER DETAILS</div>
  <div class="field" style="left:16px;top:30px;width:490px;right:22px">NAME:<span class="line"></span></div>
  <div class="field" style="left:16px;top:54px;right:22px">ADDRESS:<span class="line"></span></div>
  <div class="field" style="left:16px;top:78px;right:22px">PHONE<span class="line" style="margin-left:16px"></span></div>
</section>

<section class="abs panel order">
  <div class="abs" style="left:14px;top:10px;font-size:14.5px">PURCHASE ORDER NUMBER</div>
  <div class="abs" style="left:14px;top:49px;width:222px;border-top:1.4px solid #1d2a3a"></div>
  <div class="field" style="left:14px;top:50px;right:14px">DATE<span class="line" style="position:relative;margin-left:14px"><span style="position:absolute;left:35px;bottom:0">/</span><span style="position:absolute;left:105px;bottom:0">/</span></span></div>
  <div class="abs" style="left:14px;top:80px;font-size:14px;line-height:16px">DOCKET<br>NUMBER</div>
  <div class="abs docket-no">N° 0312</div>
</section>

<section class="abs services">
  <div class="abs col-head" style="left:65px;width:280px;text-align:center">SERVICE RENDERED</div>
  <div class="abs col-head" style="left:490px;width:250px;text-align:center">QUALITY</div>
  <div class="abs divider"></div>
  <div class="abs rule" style="left:5px;top:25px;width:747px"></div>
  <div class="abs rule" style="left:5px;top:54px;width:455px"></div>
  <div class="abs rule" style="left:5px;top:83px;width:455px"></div>
  <div class="abs rule" style="left:5px;top:111px;width:455px"></div>
  <div class="abs rule" style="left:5px;top:140px;width:455px"></div>
  <div class="abs rule" style="left:483px;top:54px;width:252px"></div>
  <div class="abs rule" style="left:483px;top:83px;width:252px"></div>
  <div class="abs rule" style="left:483px;top:111px;width:252px"></div>
  <div class="abs rule" style="left:483px;top:140px;width:252px"></div>
</section>

<p class="abs tax-note">Tax Invoce will be based on information provided on this docket.<br>Conditions on back of page</p>

<div class="abs print-name">Goods received by (Print Name)</div>
<div class="abs signed">SIGNED</div>

<div class="abs tear-line"></div>

<div class="abs company-bar">USE OF THE COMPANY</div>

<section class="abs panel vehicle">
  <div class="field" style="left:20px;top:8px;width:176px">VEHICLE:<span class="line"></span></div>
  <div class="field" style="left:208px;top:8px;width:170px">MODEL:<span class="line"></span></div>
  <div class="field" style="left:382px;top:8px;width:315px">SERIALS:<span class="line"></span></div>
  <div class="field" style="left:104px;top:35px;width:162px">KM STAR<span class="line" style="margin-left:10px"></span></div>
  <div class="field" style="left:260px;top:35px;width:178px">KM FINAL<span class="line"></span></div>
  <div class="field" style="left:412px;top:35px;width:195px">KM TRAVEL<span class="line" style="margin-left:10px"></span></div>
  <div class="field" style="left:60px;top:62px;width:350px">FUEL PURCHASE<span class="line"></span></div>
  <div class="field" style="left:356px;top:62px;width:160px">QTY<span class="line" style="margin-left:10px"></span></div>
  <div class="field" style="left:509px;top:62px;width:155px">PRICE<span class="line" style="margin-left:10px"></span></div>
</section>

<section class="abs panel axles prime">
  <div class="abs axle-label" style="top:12px">STERR AXEL</div>
  <div class="field" style="left:30px;top:25px;width:140px">FL<span class="line"></span></div>
  <div class="field" style="left:168px;top:25px;width:148px">FR<span class="line"></span></div>
  <div class="abs axle-label" style="top:59px">1ST DRIVE AXEL</div>
  <div class="field" style="left:30px;top:73px;width:140px">FL<span class="line"></span></div>
  <div class="field" style="left:168px;top:73px;width:148px">FR<span class="line"></span></div>
  <div class="abs axle-label" style="top:107px">2ND DRIVE AXEL</div>
  <div class="field" style="left:30px;top:123px;width:140px">FL<span class="line"></span></div>
  <div class="field" style="left:168px;top:123px;width:148px">FR<span class="line"></span></div>
</section>

<section class="abs panel axles trailer">
  <div class="abs axle-label" style="top:12px">1ST AXEL</div>
  <div class="field" style="left:28px;top:25px;width:140px">DS<span class="line"></span></div>
  <div class="field" style="left:164px;top:25px;width:150px">PS<span class="line"></span></div>
  <div class="abs axle-label" style="top:59px">2ND AXEL</div>
  <div class="field" style="left:28px;top:73px;width:140px">DS<span class="line"></span></div>
  <div class="field" style="left:164px;top:73px;width:150px">PS<span class="line"></span></div>
  <div class="abs axle-label" style="top:107px">3RD AXEL</div>
  <div class="field" style="left:28px;top:123px;width:140px">DS<span class="line"></span></div>
  <div class="field" style="left:164px;top:123px;width:150px">PS<span class="line"></span></div>
</section>

</body>
</html>
```